Flyer Design

we are cleaning company specialize in home cleaning, based in North Shore in Auckland (NZ).
Company name PM is initial of pure mint.
we provide professional, high standard,attention to detail service,
to make dust-free, sparkling house and no-stress family.

(business practice)--don't write this title
"colour coded cleaning system"
---we use different colour's microfiber cloths and mop heads for more hygene.
"green and clean"
---we use eco-friendly, non-toxic cleaning products for environment and your family's health.

service we offer
regular cleaning service
--weekly, fortnightly, monthly
one-off cleaning service
---move in/out cleaning
---rental inspection cleaning
---spring cleaning
---open home cleaning
---remodeling clean-up
---special occasion cleaning(event,party)

special cleaning
---window cleaning
---oven cleaning
---house washing(water blasting)

Free in home no obligation consultation and 50% off first service.
contact no; Rob and Helen 021 0847 5526,09-571-6842
e-mail info@pmhomecare.example.nz
www.pmhomecare.example.nz

we would like to see designs that use colours blue and lite pink, clean, bright and friendly image.

Target Market(s)

Woman aged between late 30th to 60th, housewives, career woman, senior etc.

Industry/Entity Type

Environment

Requirements
Should not have
• For the introduction instead of writing what I have written above verbatim, would you be able to go to our website and paraphrase/reword the introduction that's already there?

Also please don't use the picture on the website, we are planning to change the picture. Thanks.

```html
<!DOCTYPE html>
<html lang="en">
<head>
<meta charset="utf-8">
<title>PM Cleaning Services – Flyer</title>
<link rel="stylesheet" href="https://fonts.googleapis.com/css2?family=Cinzel:wght@500;600&family=Open+Sans:wght@300;400;600;700&family=Roboto+Condensed:wght@700&display=swap">
<style>
  :root{
    --blue:#1874c2;
    --blue-dark:#0f5fa6;
    --blue-text:#1d6fb8;
    --pink:#d81b6b;
    --pink-light:#e8478f;
    --magenta:#e0117f;
    --yellow:#f6ea10;
    --paper:#f1f1f3;
    --white:#ffffff;
    --ink:#444444;
    --stage:#e8e6e3;
  }
  *{box-sizing:border-box;margin:0;padding:0}
  html,body{width:1200px;height:852px;overflow:hidden}
  body{background:var(--stage);font-family:"Open Sans",Arial,sans-serif;position:relative}
  .page{position:absolute;top:74px;width:519px;height:728px;overflow:hidden;box-shadow:0 2px 6px rgba(0,0,0,.25)}
  .page--back{left:59px;background:var(--paper)}
  .page--front{left:594px;background:var(--white)}
  .abs{position:absolute}

  /* Back */
  .back-hero{left:0;top:0;width:519px;height:371px;background:var(--blue)}
  .back-hero__rule{left:0;top:371px;width:519px;height:4px;background:linear-gradient(90deg,var(--pink),#8d3c9a)}
  .offer{left:28px;top:16px;color:var(--white);font-family:"Roboto Condensed",Arial,sans-serif;font-weight:700;font-size:27.5px;line-height:36px;white-space:nowrap}
  .offer__accent{color:var(--yellow);font-size:32px}
  .photo-card{left:26px;top:116px;width:358px;height:236px;background:var(--white);border-radius:12px;overflow:hidden}
  .photo-card__photo{position:absolute;left:0;top:40px;width:358px;height:196px;background:linear-gradient(135deg,#c9c4bd,#8a7f74 55%,#3e3a38);border-radius:0 0 30px 30px}
  .ring{top:101px;width:28px;height:40px;border-radius:6px;background:linear-gradient(180deg,var(--pink-light),#a3155a)}
  .intro{left:398px;top:123px;width:98px;color:var(--white);font-size:8.3px;line-height:14.4px;text-align:center}

  .tab{left:0;height:26px;padding-left:26px;width:188px;color:var(--white);font-size:15.5px;line-height:26px;font-weight:400;background:linear-gradient(90deg,var(--pink-light),var(--pink));clip-path:polygon(0 0,176px 0,188px 13px,176px 26px,0 26px)}
  .item-title{left:26px;color:var(--blue-text);font-weight:600;font-size:10.5px}
  .item-text{left:26px;width:180px;color:var(--ink);font-size:7.6px;line-height:10.5px}
  .sub-title{left:26px;color:var(--blue-text);font-weight:600;font-size:8px}
  .freq{left:30px;top:576px;font-size:7.6px;color:var(--ink);display:flex;gap:12px}
  .freq span::before{content:"";display:inline-block;width:7px;height:7px;border-radius:50%;background:var(--pink);margin-right:3px;vertical-align:-1px}
  .oneoff{left:30px;top:606px;list-style:none;font-size:7.6px;line-height:11.7px;color:var(--ink)}
  .oneoff li::before{content:"";display:inline-block;width:6px;height:6px;border-radius:50%;background:var(--blue-text);margin-right:5px;vertical-align:0}

  .contact-bubble{left:236px;top:398px;width:112px;height:112px}
  .contact-bubble__text{left:236px;top:424px;width:104px;text-align:center;color:var(--white);font-family:"Roboto Condensed",Arial,sans-serif;font-weight:700;font-size:22px;line-height:28px}
  .team-photo{left:359px;top:401px;width:104px;height:86px;border:2px solid #cfd6de;background:linear-gradient(180deg,#e7ebef,#7fa3c6);border-radius:3px}
  .team-names{left:359px;top:490px;width:104px;text-align:center;font-size:9px;font-weight:600;color:var(--ink)}
  .contact-lines{right:43px;top:510px;text-align:right;font-size:10px;line-height:15px;color:var(--ink)}
  .contact-lines__web{font-weight:600;letter-spacing:.8px}
  .contact-phone{right:29px;top:549px;font-size:12px;font-weight:700;color:var(--magenta)}
  .promise{left:211px;top:551px;width:282px;height:128px}
  .promise__text{left:213px;top:580px;width:278px;text-align:center;color:var(--white);font-weight:700;font-size:13.4px;line-height:22px;white-space:nowrap}
  .tagline{left:0;top:692px;width:519px;text-align:center;color:var(--magenta);font-weight:300;font-size:17px}

  /* Front */
  .front-hero{left:0;top:0;width:518px;height:259px;background:var(--blue)}
  .brand{left:0;top:28px;width:518px;text-align:center;color:var(--white);font-family:"Cinzel",Georgia,serif;font-weight:600;font-size:36px;letter-spacing:.5px;white-space:nowrap}
  .front-sub{left:0;top:102px;width:518px;text-align:center;color:#eef4fb;font-weight:300;font-size:23px}
  .badge{top:144px;width:148px;height:96px}
  .badge__label{top:144px;width:148px;height:96px;display:flex;align-items:center;justify-content:center;padding-left:4px}
  .badge__text{display:block;text-align:center;color:var(--white);font-size:16.5px;line-height:19px}
  .badge__text small{display:block;font-size:13.5px;font-weight:600;line-height:18px}
  .contact-strip{left:0;top:259px;width:518px;height:56px;background:var(--paper)}
  .strip-lines{left:32px;top:267px;font-size:11px;line-height:16px;color:var(--ink)}
  .strip-lines b{font-weight:700;letter-spacing:.8px}
  .strip-phone{right:22px;top:277px;font-size:20px;font-weight:700;color:#3b3b3b}
  .tile{background:#ccc}
  .front-foot{left:0;top:666px;width:518px;height:62px;background:var(--blue)}
  .front-foot__text{left:0;top:675px;width:518px;text-align:center;color:var(--white);font-family:"Cinzel",Georgia,serif;font-weight:600;font-size:31px;white-space:nowrap}
</style>
</head>
<body>

<section class="page page--back" aria-label="Flyer back">
  <div class="abs back-hero"></div>
  <div class="abs back-hero__rule"></div>
  <h2 class="abs offer">Free in home No obligation<br>consultation and <span class="offer__accent">50% OFF</span> first service</h2>

  <div class="abs photo-card">
    <div class="photo-card__photo" role="img" aria-label="Photo of a cleaner wiping a kitchen bench"></div>
  </div>
  <div class="abs ring" style="left:81px"></div><div class="abs ring" style="left:116px"></div>
  <div class="abs ring" style="left:173px"></div><div class="abs ring" style="left:208px"></div>
  <div class="abs ring" style="left:267px"></div><div class="abs ring" style="left:302px"></div>

  <p class="abs intro">We strive to provide a professional, high quality home cleaning services at an affordable price. We do our best to meet every customers requirement whatever your personal cleaning needs are. Because we always aim to make your home sparkle clean and healthy place to live. We love the job!</p>

  <h3 class="abs tab" style="top:388px">Business Practice</h3>
  <p class="abs item-title" style="top:424px">Colour Coded Cleaning System</p>
  <p class="abs item-text" style="top:441px">We use different colour's microfiber cloths and mop heads for more hygene.</p>
  <p class="abs item-title" style="top:470px">Green And Clean</p>
  <p class="abs item-text" style="top:489px">We use eco-friendly, non-toxic cleaning for environment and your family's health.</p>

  <h3 class="abs tab" style="top:527px">Service We Offer</h3>
  <p class="abs sub-title" style="top:561px">Regular Cleaning Service</p>
  <p class="abs freq"><span>Weekly,</span><span>Fortnightly,</span><span>Monthly</span></p>
  <p class="abs sub-title" style="top:592px">One-off Cleaning Service</p>
  <ul class="abs oneoff">
    <li>Move in/out cleaning</li>
    <li>Rental inspection cleaning</li>
    <li>Spring cleaning</li>
    <li>Open home cleaning</li>
    <li>Remodeling clean-up</li>
    <li>Special occasion cleaning (event, party)</li>
  </ul>

  <svg class="abs contact-bubble" viewBox="0 0 112 112" aria-hidden="true">
    <defs><radialGradient id="bubbleFill" cx="40%" cy="30%" r="75%"><stop offset="0" stop-color="#f06aa8"/><stop offset="1" stop-color="#b0105a"/></radialGradient></defs>
    <path d="M92 84 L110 106 L78 94 Z" fill="#d6d6da"/>
    <circle cx="52" cy="54" r="51" fill="#d6d6da"/>
    <path d="M88 82 L104 102 L76 90 Z" fill="url(#bubbleFill)"/>
    <circle cx="52" cy="54" r="46" fill="url(#bubbleFill)"/>
  </svg>
  <p class="abs contact-bubble__text">Contact<br>Us</p>

  <div class="abs team-photo" role="img" aria-label="Portrait of Rob and Helen"></div>
  <p class="abs team-names">Rob &amp; Helen</p>
  <p class="abs contact-lines">Email: info@pmhomecare.example.nz<br><span class="contact-lines__web">www.pmhomecare.example.nz</span></p>
  <p class="abs contact-phone">021 0847 5526,&nbsp; 09-571-6842</p>

  <svg class="abs promise" viewBox="0 0 282 128" aria-hidden="true">
    <defs><linearGradient id="promiseFill" x1="0" y1="0" x2="0" y2="1"><stop offset="0" stop-color="#2a86d4"/><stop offset="1" stop-color="#1465b0"/></linearGradient></defs>
    <path d="M10 20 H66 L78 0 L84 20 H272 Q280 20 280 30 V116 Q280 126 270 126 H12 Q2 126 2 116 V30 Q2 20 10 20 Z" fill="url(#promiseFill)" stroke="#c9d4e0" stroke-width="2"/>
  </svg>
  <p class="abs promise__text">We provide professional, high<br>standard, attention to detail service,<br>to make dust-free, sparkling house<br>and no-stress family.</p>

  <p class="abs tagline">Husband and wife team.&nbsp; Dependable, friendly and honest</p>
</section>

<section class="page page--front" aria-label="Flyer front">
  <div class="abs front-hero"></div>
  <h1 class="abs brand">PM CLEANING SERVICES</h1>
  <p class="abs front-sub">The Park's Special Home Cleaning Services</p>

  <svg class="abs badge" style="left:24px" viewBox="0 0 148 96" aria-hidden="true"><defs><radialGradient id="badgeFill" cx="45%" cy="30%" r="75%"><stop offset="0" stop-color="#ea5a9c"/><stop offset="1" stop-color="#b3125d"/></radialGradient></defs><ellipse cx="74" cy="49" rx="72" ry="46" fill="#c9c9cf"/><ellipse cx="74" cy="47" rx="70" ry="44" fill="#fff"/><ellipse cx="76" cy="48" rx="62" ry="38" fill="url(#badgeFill)"/></svg>
  <p class="abs badge__label" style="left:24px"><span class="badge__text">WINDOW<br>CLEANING</span></p>
  <svg class="abs badge" style="left:180px" viewBox="0 0 148 96" aria-hidden="true"><ellipse cx="74" cy="49" rx="72" ry="46" fill="#c9c9cf"/><ellipse cx="74" cy="47" rx="70" ry="44" fill="#fff"/><ellipse cx="76" cy="48" rx="62" ry="38" fill="url(#badgeFill)"/></svg>
  <p class="abs badge__label" style="left:180px"><span class="badge__text">OVEN<br>CLEANING</span></p>
  <svg class="abs badge" style="left:342px" viewBox="0 0 148 96" aria-hidden="true"><ellipse cx="74" cy="49" rx="72" ry="46" fill="#c9c9cf"/><ellipse cx="74" cy="47" rx="70" ry="44" fill="#fff"/><ellipse cx="76" cy="48" rx="62" ry="38" fill="url(#badgeFill)"/></svg>
  <p class="abs badge__label" style="left:342px"><span class="badge__text">HOUSE<br>WASHING<small>(Water blasting)</small></span></p>

  <div class="abs contact-strip"></div>
  <p class="abs strip-lines">Email: info@pmhomecare.example.nz<br><b>www.pmhomecare.example.nz</b></p>
  <p class="abs strip-phone">021 0847 5526,&nbsp; 09-571-6842</p>

  <div class="abs tile" style="left:0;top:316px;width:253px;height:183px;background:linear-gradient(135deg,#6e6258,#2f2c2b 70%)" role="img" aria-label="Photo of a tidy bedroom with a sofa"></div>
  <div class="abs tile" style="left:256px;top:316px;width:262px;height:183px;background:linear-gradient(135deg,#eceef0,#cfd3d6)" role="img" aria-label="Photo of a gloved hand wiping wall tiles"></div>
  <div class="abs tile" style="left:0;top:501px;width:253px;height:164px;background:linear-gradient(135deg,#a9a39c,#e9e7e4 60%,#d5d2ce)" role="img" aria-label="Photo of a clean bathroom with bath and vanity"></div>
  <div class="abs tile" style="left:256px;top:501px;width:262px;height:164px;background:linear-gradient(135deg,#dfe9f2,#a9bdd0)" role="img" aria-label="Photo of a gloved hand cleaning a window"></div>

  <div class="abs front-foot"></div>
  <p class="abs front-foot__text">PM IS INITIAL OF PURE MINT</p>
</section>

</body>
</html>
```